Luxury Residential Real Estate Flyer

We need a residential real estate flyer template design for a company called The Marlowe Circle. We operate across the Gulf South US. We have a logo and colors that we have adopted. We are looking for a template that has text boxes that can be changed and pictures that can be swapped out to be used on multiple properties.

Target Market(s)

Luxury residential real estate buyers

Number of Pages Required

3 page

Requirements
Must have
• Main page + 2 supporting pages. Contact information boxes listed for two people. Needs a place to add amenities about the property. Should also have space allotted for 6-8 pictures throughout the flyer.
Nice to have
• Maybe a map

```html
<!DOCTYPE html>
<html lang="en">
<head>
<meta charset="utf-8">
<title>The Marlowe Circle – Property Flyer</title>
<link href="https://fonts.googleapis.com/css2?family=Arimo:wght@400;700&display=swap" rel="stylesheet">
<style>
  :root{
    --paper:#ffffff;
    --orange:#e8731d;
    --orange-strong:#e4620c;
    --brown:#4f330d;
    --brown-line:#6a4a22;
    --taupe:#6d6051;
    --ink:#2b2b2b;
    --map:#eeefed;
    --map-road:#d9dbd8;
    --pin:#e0372b;
  }
  *{margin:0;padding:0;box-sizing:border-box}
  html,body{width:1200px;height:1200px;overflow:hidden}
  body{
    background:linear-gradient(#e3e3e5,#f1f1f2);
    font-family:"Arimo",Arial,sans-serif;
    color:var(--ink);
    position:relative;
  }
  .page{
    position:absolute;top:350px;width:424px;height:577px;
    background:var(--paper);
    transform:scale(.868);transform-origin:top left;
    box-shadow:0 1px 3px rgba(0,0,0,.12);
    overflow:hidden;
  }
  .page--cover{left:26px}
  .page--gallery{left:416px}
  .page--contacts{left:806px}
  .abs{position:absolute}
  .photo{position:absolute}

  /* cover */
  .brand{left:30px;top:30px;display:flex;align-items:center;gap:8px}
  .brand__mark{width:14px;height:14px;background:var(--orange)}
  .brand__name{font-size:17px;font-weight:700;color:var(--brown);letter-spacing:.02em}
  .services{left:310px;top:22px;border-left:2px solid var(--orange);padding-left:9px;
    font-size:6.5px;font-weight:700;letter-spacing:.22em;color:var(--orange);line-height:12px}
  .hero{left:0;top:82px;width:424px;height:250px;
    background:
      linear-gradient(to bottom,rgba(0,0,0,0) 72%,#1c2a20 86%,#141d18 100%),
      linear-gradient(to right,#13233a 0%,#1d3552 18%,#c8924f 32%,#e7b46a 45%,#b07f45 56%,#233a58 68%,#16263d 100%);}
  .features{left:25px;top:344px;width:150px}
  .label{font-size:7.5px;font-weight:700;color:var(--orange);margin-bottom:6px}
  .features ul{list-style:none;font-size:7px;line-height:15px;margin-bottom:16px}
  .features p{font-size:7px;line-height:11px;color:var(--ink)}
  .side-photo{left:188px;top:340px;width:236px;height:157px;
    background:
      linear-gradient(to bottom,rgba(0,0,0,0) 78%,#44603c 86%,#35502f 100%),
      linear-gradient(to bottom,#5d73b4 0%,#7f8fc3 40%,#a9a6c4 58%,#d5c8c4 70%,#8b7d74 78%);}
  .rule-brown{left:0;top:526px;width:252px;height:2px;background:var(--brown-line)}
  .rule-orange{left:252px;top:526px;width:172px;height:2px;background:var(--orange)}
  .social{left:280px;top:536px;display:flex;gap:3px;align-items:center}
  .social i{display:block;width:11px;height:11px;background:var(--brown-line);border:1px solid var(--orange)}
  .social span{margin-left:5px;font-size:6.5px;color:var(--ink)}

  /* gallery */
  .living{left:0;top:0;width:424px;height:320px;
    background:
      linear-gradient(to bottom,rgba(255,255,255,0) 55%,#f2f2f0 70%,#e6e6e4 100%),
      linear-gradient(to right,#dcdcda 0%,#5f7c44 8%,#7f9a5c 26%,#4f5a4c 30%,#8aa36a 34%,#9db27c 62%,#3f4440 66%,#7f9a5c 70%,#5c7740 92%,#e2e2e0 100%);}
  .body-copy{left:17px;top:330px;width:192px;font-size:6.6px;line-height:12.5px;color:var(--ink)}
  .map{left:16px;top:458px;width:194px;height:86px;border:1px solid #e2e2e2;overflow:hidden;background:var(--map)}
  .map svg{display:block}
  .frame{left:222px;top:283px;width:202px;height:294px;background:var(--brown)}
  .lounge{left:234px;top:298px;width:178px;height:134px;
    background:linear-gradient(to bottom,#e9e7e3 0%,#d7d3cc 55%,#b8ab98 75%,#8a7d6c 100%)}
  .den{left:234px;top:437px;width:178px;height:125px;
    background:linear-gradient(to bottom,#ecebe9 0%,#c9c8c4 45%,#9c9892 70%,#7e7a73 100%)}

  /* contacts */
  .bedroom{left:0;top:0;width:248px;height:196px;
    background:linear-gradient(to bottom,#e7e4dc 0%,#d8d2c4 55%,#6b4a30 78%,#8e2a2c 100%)}
  .kitchen{left:0;top:199px;width:248px;height:189px;
    background:linear-gradient(to bottom,#f1f1f1 0%,#dcdad7 45%,#a4a09c 70%,#d8d8d6 100%)}
  .salon{left:0;top:392px;width:248px;height:185px;
    background:linear-gradient(to bottom,#e8e6e1 0%,#d9d4c8 45%,#bdb8ae 70%,#6f6c67 100%)}
  .card{position:absolute;left:258px;width:158px;height:276px;background:var(--taupe);border:4px solid var(--orange-strong)}
  .card--first{top:10px}
  .card--second{top:290px}
  .card__portrait{position:absolute;left:33px;top:38px;width:76px;height:96px;
    background:linear-gradient(#d4d4d4,#8e8e8e)}
  .card__info{position:absolute;left:35px;top:154px;font-size:7px;line-height:15px;color:#fff}
  .card__name{font-weight:700;font-size:7.5px}
  .card__info b{color:var(--orange);font-weight:400;margin-right:3px}
</style>
</head>
<body>

<section class="page page--cover">
  <div class="abs brand"><span class="brand__mark"></span><span class="brand__name">The Marlowe Circle</span></div>
  <div class="abs services">REAL ESTATE<br>BROKERAGE<br>DEVELOPMENT</div>
  <div class="photo hero" role="img" aria-label="Modern glass-fronted house lit at dusk with pool"></div>
  <div class="abs features">
    <h3 class="label">Property features</h3>
    <ul><li>- 8800 Square Feet Internal</li><li>- 42132 Square Feet Plot</li></ul>
    <h3 class="label">Property description</h3>
    <p>Situated at the end of a long gated drive on one of Beverly Hills most legendary streets sits a spectacular modern glass framed house with high ceilings and spectacular views, ideal for entertaining with vast living area and spacious modern kitchen, media room, wine cellar, sweeping rear pavilion with outdoor bar, grill and resistance pool.</p>
  </div>
  <div class="photo side-photo" role="img" aria-label="Side view of the modern house at twilight"></div>
  <div class="abs rule-brown"></div><div class="abs rule-orange"></div>
  <div class="abs social"><i></i><i></i><i></i><i></i><span>themarlowecircle</span></div>
</section>

<section class="page page--gallery">
  <div class="photo living" role="img" aria-label="Open living room with glass walls and chandelier"></div>
  <p class="abs body-copy">Lorem ipsum dolor sit amet, consectetuer adipiscing elit, sed diam nonummy nibh euismod tincidunt ut laoreet dolore magna aliquam erat volutpat. Ut wisi enim ad minim veniam, quis nostrud exerci tation ullamcorper suscipit lobortis nisl ut aliquip ex ea commodo consequat. Duis autem vel eum iriure dolor in hendrerit in vulputate velit esse molestie consequat, vel illum dolore eu feugiat nulla facilisis at vero eros et accumsan et iusto odio dignissim qui blandit present luptatum zzril delenit augue duis dolore te feugait nulla facilisi.</p>
  <div class="map" role="img" aria-label="Street map showing the property location">
    <svg width="192" height="84" viewBox="0 0 192 84" aria-hidden="true">
      <rect width="192" height="84" fill="#eeefed"/>
      <g transform="translate(88 6)">
        <path d="M5 0a5 5 0 0 1 5 5c0 4-5 10-5 10S0 9 0 5a5 5 0 0 1 5-5z" fill="#e0372b"/>
        <circle cx="5" cy="5" r="1.8" fill="#fff"/>
      </g>
    </svg>
  </div>
  <div class="abs frame"></div>
  <div class="photo lounge" role="img" aria-label="Lounge with built-in shelving"></div>
  <div class="photo den" role="img" aria-label="Family room with sectional sofa"></div>
</section>

<section class="page page--contacts">
  <div class="photo bedroom" role="img" aria-label="Master bedroom with canopy bed"></div>
  <div class="photo kitchen" role="img" aria-label="Modern kitchen with island and glass stair"></div>
  <div class="photo salon" role="img" aria-label="Round lounge with pendant light"></div>
  <div class="card card--first">
    <div class="card__portrait" role="img" aria-label="Agent headshot"></div>
    <div class="card__info"><div class="card__name">Daniel Corvell</div><div><b>H:</b>(504) 555-0148</div><div><b>E:</b>agents@marlowecircle.com</div></div>
  </div>
  <div class="card card--second">
    <div class="card__portrait" role="img" aria-label="Agent headshot"></div>
    <div class="card__info"><div class="card__name">Simon Aldway</div><div><b>H:</b>(504) 555-0148</div><div><b>E:</b>agents@marlowecircle.com</div></div>
  </div>
</section>

</body>
</html>
```